Design a New Business Card for Our Company

We are looking for fresh, unique, and a modern business card that reflects our roots as digital marketing agency focused on SEM.

Industry/Entity Type

Marketing

Contact Information for Business Card

looking for very unique out of the box designs. clean and modern that compliments our logo

Requirements
Must have
• colors should match our logo
• Front should have name, address, email, and phone/fax of the person, phone/fax are the same number
• back should have our url

```html
<!DOCTYPE html>
<html lang="en">
<head>
<meta charset="utf-8">
<title>Brightwave Media – Business Card</title>
<link rel="stylesheet" href="https://fonts.googleapis.com/css2?family=Montserrat:wght@400;500;600;700&display=swap">
<style>
  :root {
    --stage: #e9ebee;
    --card-blue: #5b9bd5;
    --accent-blue: #4a8fd4;
    --bright-blue: #1ea7e8;
    --band-grey: #b9bbbd;
    --text-grey: #9a9c9f;
    --logo-grey: #a8aaad;
    --white: #ffffff;
  }
  * { box-sizing: border-box; margin: 0; padding: 0; }
  html, body {
    width: 1200px; height: 900px; overflow: hidden;
    background: var(--stage);
    font-family: "Montserrat", sans-serif;
  }
  .stage { position: relative; width: 1200px; height: 900px; }

  .card {
    position: absolute; width: 540px; height: 310px;
    border-radius: 20px; overflow: hidden;
    box-shadow: 0 10px 28px rgba(0,0,0,.16);
  }

  /* Back of card */
  .card--back { left: 80px; top: 90px; background: var(--card-blue); }
  .back-brand {
    position: absolute; left: 0; right: 0; top: 104px;
    display: flex; align-items: center; justify-content: center; gap: 16px;
    color: var(--white); font-weight: 600; font-size: 36px; letter-spacing: .5px;
    white-space: nowrap;
  }
  .back-brand__dot { width: 26px; height: 26px; border-radius: 50%; background: var(--white); }
  .back-url {
    position: absolute; left: 0; right: 0; bottom: 34px; text-align: center;
    color: var(--white); font-size: 15px; font-weight: 500;
  }
  .back-strip { position: absolute; left: 0; right: 0; bottom: 0; height: 22px; background: var(--white); }
  .back-strip__grey { position: absolute; left: 52%; width: 31%; bottom: 16px; height: 14px; background: var(--band-grey); }
  .back-strip__line { position: absolute; left: 51.4%; width: 0.6%; bottom: 14px; height: 16px; background: var(--bright-blue); }

  /* Front of card */
  .card--front { left: 580px; top: 490px; background: var(--white); }
  .front-brand {
    position: absolute; left: 34px; top: 74px;
    display: flex; align-items: center; gap: 10px;
    color: var(--logo-grey); font-weight: 700; font-size: 23px; letter-spacing: -.3px;
    white-space: nowrap;
  }
  .front-brand__dot { width: 18px; height: 18px; border-radius: 50%; background: var(--logo-grey); }

  .holder { position: absolute; right: 40px; top: 34px; text-align: right; white-space: nowrap; }
  .holder__name { color: var(--accent-blue); font-weight: 600; font-size: 21px; }
  .holder__role { color: var(--text-grey); font-size: 11px; margin-top: 2px; }
  .holder-tab { position: absolute; right: 0; top: 32px; width: 28px; height: 30px; background: var(--card-blue); }
  .holder-rule { position: absolute; right: 40px; top: 98px; width: 200px; height: 1.5px; background: var(--accent-blue); }

  .address {
    position: absolute; right: 40px; top: 114px; text-align: right;
    color: var(--text-grey); font-size: 13px; line-height: 1.45;
  }

  .contacts-rule { position: absolute; left: 34px; top: 168px; width: 240px; height: 1.5px; background: var(--accent-blue); }
  .contacts { position: absolute; left: 34px; top: 178px; list-style: none; }
  .contacts li {
    display: flex; align-items: center; gap: 10px;
    color: var(--text-grey); font-size: 13px; line-height: 20px; white-space: nowrap;
  }
  .contacts svg { width: 12px; height: 12px; flex: none; }
  .contacts strong { color: var(--accent-blue); font-weight: 600; }

  .front-band { position: absolute; left: 0; right: 0; bottom: 0; height: 34px; }
  .front-band__blue-left { position: absolute; left: 0; width: 46%; bottom: 6px; height: 14px; background: var(--bright-blue); }
  .front-band__grey { position: absolute; left: 46%; width: 34%; bottom: 6px; height: 14px; background: var(--band-grey); }
  .front-band__blue-right { position: absolute; left: 80%; right: 0; bottom: 6px; height: 14px; background: var(--bright-blue); }
  .front-band__base { position: absolute; left: 0; right: 0; bottom: 0; height: 6px; background: var(--bright-blue); }
</style>
</head>
<body>
<main class="stage">

  <section class="card card--back" aria-label="Card back">
    <div class="back-brand"><span class="back-brand__dot"></span>Brightwave Media</div>
    <p class="back-url">www.brightwavemedia.com</p>
    <div class="back-strip"></div>
    <div class="back-strip__grey"></div>
    <div class="back-strip__line"></div>
  </section>

  <section class="card card--front" aria-label="Card front">
    <div class="front-brand"><span class="front-brand__dot"></span>Brightwave Media</div>

    <div class="holder-tab"></div>
    <div class="holder">
      <p class="holder__name">Marla Keaton</p>
      <p class="holder__role">Director</p>
    </div>
    <div class="holder-rule"></div>

    <p class="address">PO Box 317 Fairview<br>NSW Australia 2090</p>

    <div class="contacts-rule"></div>
    <ul class="contacts">
      <li>
        <svg viewBox="0 0 24 24" fill="#4a8fd4"><path d="M6.6 10.8a15 15 0 0 0 6.6 6.6l2.2-2.2a1 1 0 0 1 1-.25 11.4 11.4 0 0 0 3.6.6 1 1 0 0 1 1 1V20a1 1 0 0 1-1 1A17 17 0 0 1 3 4a1 1 0 0 1 1-1h3.5a1 1 0 0 1 1 1c0 1.250.2 2.450.6 3.6a1 1 0 0 1-.25 1z"/></svg>
        +330 5812-4409
      </li>
      <li>
        <svg viewBox="0 0 24 24" fill="#4a8fd4"><rect x="6" y="3" width="12" height="6" rx="1"/><rect x="3" y="10" width="18" height="8" rx="2"/><rect x="7" y="15" width="10" height="6" fill="#fff" stroke="#4a8fd4" stroke-width="2"/></svg>
        +330 5812-4410
      </li>
      <li>
        <svg viewBox="0 0 24 24" fill="none" stroke="#4a8fd4" stroke-width="2"><rect x="3" y="5" width="18" height="14" rx="1"/><path d="M3 6l9 7 9-7"/></svg>
        info@brightwavemedia.com
      </li>
      <li>
        <svg viewBox="0 0 24 24" fill="none" stroke="#4a8fd4" stroke-width="2"><circle cx="12" cy="12" r="9"/><path d="M3 12h18M12 3c3 3 3 15 0 18M12 3c-3 3-3 15 0 18"/></svg>
        <span>www.<strong>brightwavemedia</strong>.com</span>
      </li>
    </ul>

    <div class="front-band">
      <div class="front-band__blue-left"></div>
      <div class="front-band__grey"></div>
      <div class="front-band__blue-right"></div>
      <div class="front-band__base"></div>
    </div>
  </section>

</main>
</body>
</html>
```